Business Card Design

Art work over image with business name and phone number. We do automotive wire repair. Some sort of auto theme. Thanks!
Updates

I would like to see the images I uploaded in the card.  Thanks!

Target Market(s)

Auto body repair shops

Industry/Entity Type

Automotive

Contact Information for Business Card

CIRCUIT BARON

480-395-2146

Requirements
Nice to have
• Raised lettering?

```html
<!DOCTYPE html>
<html lang="en">
<head>
<meta charset="utf-8">
<title>Circuit Baron – Business Card</title>
<link href="https://fonts.googleapis.com/css2?family=Orbitron:wght@600;800&family=Open+Sans:wght@400;700&display=swap" rel="stylesheet">
<style>
  :root {
    --page-bg: #3a3b3e;
    --card-black: #0a0a0b;
    --slate-blue: #46557a;
    --slate-blue-dark: #2c3550;
    --silver: #d9dbe0;
    --silver-dark: #8a8e96;
    --text-light: #f2f3f5;
    --text-muted: #d0d2d6;
    --car-light: #9ea3ab;
    --car-dark: #1a1c20;
  }
  html, body {
    margin: 0;
    padding: 0;
    width: 1200px;
    height: 1000px;
    overflow: hidden;
    background: var(--page-bg);
  }
  .canvas {
    position: relative;
    width: 1200px;
    height: 1000px;
  }
  .card {
    position: absolute;
    left: 250px;
    width: 700px;
    height: 400px;
    background: var(--card-black);
    border-radius: 6px;
    overflow: hidden;
    box-shadow: 0 10px 30px rgba(0,0,0,0.45);
  }
  .card--front { top: 60px; }
  .card--back { top: 540px; }

  .front-bands {
    position: absolute;
    inset: 0;
  }
  .brand-name {
    position: absolute;
    margin: 0;
    font-family: "Orbitron", sans-serif;
    font-weight: 800;
    color: var(--text-light);
    letter-spacing: 3px;
    line-height: 1.05;
  }
  .card--front .brand-name {
    left: 60px;
    top: 60px;
    font-size: 40px;
  }
  .shop-type {
    position: absolute;
    right: 44px;
    top: 140px;
    margin: 0;
    font-family: "Orbitron", sans-serif;
    font-weight: 600;
    font-size: 26px;
    line-height: 1.15;
    letter-spacing: 2px;
    color: var(--text-light);
    text-align: right;
    text-transform: uppercase;
  }
  .services {
    position: absolute;
    right: 44px;
    top: 214px;
    margin: 0;
    font-family: "Open Sans", sans-serif;
    font-size: 17px;
    line-height: 1.25;
    color: var(--text-muted);
    text-align: right;
  }
  .services strong { color: var(--text-light); }
  .phone {
    position: absolute;
    right: 44px;
    bottom: 34px;
    margin: 0;
    font-family: "Orbitron", sans-serif;
    font-weight: 800;
    font-size: 38px;
    line-height: 1.2;
    letter-spacing: 3px;
    color: var(--text-light);
    white-space: nowrap;
  }

  .car-visual {
    position: absolute;
    left: 70px;
    top: 40px;
    width: 560px;
    height: 320px;
    border-radius: 140px / 110px;
    background: radial-gradient(ellipse at 50% 50%, var(--car-light) 0%, #5d626a 40%, var(--car-dark) 75%, var(--card-black) 100%);
    opacity: 0.85;
  }
  .card--back .brand-name {
    left: 0;
    right: 0;
    top: 172px;
    text-align: center;
    font-size: 44px;
  }
</style>
</head>
<body>
<main class="canvas">

  <section class="card card--front" aria-label="Business card front">
    <svg class="front-bands" viewBox="0 0 700 400" width="700" height="400" aria-hidden="true">
      <defs>
        <linearGradient id="blueBand" x1="0" y1="0" x2="1" y2="1">
          <stop offset="0" stop-color="var(--slate-blue)"/>
          <stop offset="1" stop-color="var(--slate-blue-dark)"/>
        </linearGradient>
        <linearGradient id="silverEdge" x1="0" y1="0" x2="1" y2="0">
          <stop offset="0" stop-color="var(--silver-dark)"/>
          <stop offset="0.5" stop-color="var(--silver)"/>
          <stop offset="1" stop-color="var(--silver-dark)"/>
        </linearGradient>
      </defs>
      <path d="M0 0 H700 V110 C540 110 400 130 330 200 C270 260 250 330 240 400 H0 Z" fill="url(#blueBand)"/>
      <path d="M700 110 C540 110 400 130 330 200 C270 260 250 330 240 400" fill="none" stroke="url(#silverEdge)" stroke-width="9"/>
    </svg>

    <h1 class="brand-name">CIRCUIT<br>BARON</h1>

    <p class="shop-type">Auto Body<br>Repair Shop</p>
    <p class="services"><strong>specialized in</strong><br>automotive wire repair<br>auto theme</p>
    <p class="phone">480-395-2146</p>
  </section>

  <section class="card card--back" aria-label="Business card back">
    <div class="car-visual" role="img" aria-label="See-through cutaway view of a silver car showing its engine and wiring"></div>
    <h2 class="brand-name">CIRCUIT BARON</h2>
  </section>

</main>
</body>
</html>
```